Technical Communications firm needs an article turned into a white paper

We want to redesign a 3-part blog series into a white paper that we can print for a conference. I've consolidated the three posts into the attached Word document.

We are looking for a light, easy to read design. Good use of graphics to support the message. I've added the graphics we used in the original post.

You can view them at
http://www.lanternquill.com/blog/are-you-satisfied-with-your-dita-solution/

Target Market(s)

Product managers from High-tech, Finance, and Medical industries.

Industry/Entity Type

Information Technology

Colors

Designer to choose colors to be used in the design.

Requirements
Must have
• Must be modern, light, easy to read and slick design. Try to incorporate the graphics provided, but feel free to add more. Must retain the lists and tables.
• Must align with our website/brand.
• Must be easy to read. So not too busy.
• Please move all footnotes to endnotes. You'll need to rework the numbering.
Nice to have
• Awesome coverpage.
Should not have
• Hokey clipart. Not too heavy or hard to read.

```html
<!DOCTYPE html>
<html lang="en">
<head>
<meta charset="utf-8">
<title>Are You Satisfied With Your DITA Solution? – Lantern Quill</title>
<link rel="stylesheet" href="https://fonts.googleapis.com/css2?family=Titillium+Web:wght@400;600;700&family=Open+Sans:wght@400&display=swap">
<style>
  :root {
    --page-bg: #e6e7e9;
    --paper: #ffffff;
    --paper-shade: #f1f2f4;
    --sky: #1ba3d8;
    --navy: #1f3c8c;
    --slate: #4f5a60;
    --slate-dark: #394247;
    --chalk-gold: rgba(232, 205, 70, .38);
    --warm-skin: rgba(196, 120, 80, .55);
    --auburn: rgba(150, 60, 30, .5);
    --shirt: rgba(205, 210, 215, .55);
    --ink: #3a3f44;
    --rule: #55595e;
  }
  * { box-sizing: border-box; margin: 0; padding: 0; }
  html, body { width: 1200px; height: 804px; overflow: hidden; background: var(--page-bg); }
  .canvas { position: relative; width: 1200px; height: 804px; }

  .cover {
    position: absolute; left: 330px; top: 20px;
    width: 540px; height: 764px;
    background: var(--paper);
    box-shadow: 0 4px 18px rgba(0,0,0,.18);
    overflow: hidden;
    font-family: "Titillium Web", sans-serif;
  }

  .brand {
    position: absolute; top: 42px; left: 0; width: 100%;
    display: flex; justify-content: center; align-items: center; gap: 10px;
  }
  .brand-dot { width: 34px; height: 34px; border-radius: 50%; background: var(--navy); }
  .brand-name { font-weight: 700; font-size: 20px; color: var(--navy); letter-spacing: .3px; }

  .band-top, .band-mid { position: absolute; left: 0; width: 100%; z-index: 2; }
  .band-top { top: 112px; height: 16px; }
  .band-mid { top: 472px; height: 16px; }

  .hero-photo {
    position: absolute; top: 118px; left: 0; width: 100%; height: 356px;
    background:
      radial-gradient(ellipse 90px 70px at 410px 190px, var(--warm-skin), transparent 75%),
      radial-gradient(ellipse 80px 70px at 410px 265px, var(--auburn), transparent 75%),
      radial-gradient(ellipse 150px 60px at 420px 350px, var(--shirt), transparent 75%),
      radial-gradient(ellipse 200px 130px at 180px 110px, var(--chalk-gold), transparent 75%),
      radial-gradient(ellipse 100px 90px at 130px 250px, var(--chalk-gold), transparent 75%),
      linear-gradient(135deg, var(--slate) 0%, var(--slate-dark) 100%);
  }

  .facets { position: absolute; top: 488px; left: 0; width: 100%; height: 170px; }

  .headline { position: absolute; top: 514px; left: 0; width: 100%; text-align: center; }
  .headline-kicker { font-size: 17px; font-weight: 400; color: var(--ink); letter-spacing: .3px; line-height: 1.2; }
  .headline-main { font-size: 34px; font-weight: 700; line-height: 1.1; letter-spacing: .3px; }
  .headline-main .accent { color: var(--sky); }
  .headline-main .strong { color: var(--navy); }

  .intro {
    position: absolute; top: 598px; left: 80px; width: 380px;
    border-top: 1px solid var(--rule); padding-top: 8px;
    font-family: "Open Sans", sans-serif; font-size: 11px; line-height: 1.45;
    color: var(--ink); text-align: center;
  }

  .footer-rule { position: absolute; left: 0; width: 100%; background: var(--navy); }
  .footer-rule.upper { top: 664px; height: 4px; }
  .footer-rule.lower { top: 714px; height: 4px; }
  .footer-band {
    position: absolute; top: 670px; left: 0; width: 100%; height: 42px;
    background: var(--sky);
    display: flex; align-items: center; justify-content: center;
  }
  .footer-url { color: #fff; font-size: 12px; letter-spacing: 2.4px; }
</style>
</head>
<body>
<main class="canvas">
  <article class="cover">
    <header class="brand">
      <span class="brand-dot"></span>
      <span class="brand-name">LANTERNQUILL.com</span>
    </header>

    <div class="hero-photo" role="img" aria-label="Photo: chalkboard with hand-drawn yellow star ratings beside tick boxes, the one-star box checked, and a doubtful bearded man glancing at them"></div>

    <svg class="band-top" viewBox="0 0 540 16" preserveAspectRatio="none" aria-hidden="true">
      <rect x="0" y="0" width="540" height="6" fill="#1ba3d8"/>
      <polygon points="258,6 282,6 270,14" fill="#1ba3d8"/>
    </svg>

    <svg class="band-mid" viewBox="0 0 540 16" preserveAspectRatio="none" aria-hidden="true">
      <rect x="0" y="2" width="540" height="5" fill="#1ba3d8"/>
      <polygon points="258,7 282,7 270,15" fill="#1ba3d8"/>
    </svg>

    <svg class="facets" viewBox="0 0 540 170" preserveAspectRatio="none" aria-hidden="true">
      <polygon points="0,0 180,0 90,170 0,120" fill="#f1f2f4"/>
      <polygon points="360,0 540,0 540,150 430,170" fill="#f1f2f4"/>
    </svg>

    <div class="headline">
      <p class="headline-kicker">ARE YOU SATISFIED WITH</p>
      <h1 class="headline-main"><span class="accent">YOUR DITA</span> <span class="strong">SOLUTION?</span></h1>
    </div>

    <p class="intro">We design innovative, scalable, and sustainable intelligent content solutions for authoring, managing, and publishing high-value content.</p>

    <div class="footer-rule upper"></div>
    <div class="footer-band"><span class="footer-url">www.lanternquill.com</span></div>
    <div class="footer-rule lower"></div>
  </article>
</main>
</body>
</html>
```